Letterhead design for Dental Practice - Ashby Lane Dental Care

Letterhead for Private Dental Practice. To be used for all official correspondance and for printing treatment details on to be given to patients.

Target Market(s)

Private dental patients

Industry/Entity Type

Dental Clinic

Font styles to use
Other font styles liked:
• nexa-light

Colors
33a6d7
1c66ac
85abd2

Requirements
Must have
• info in the footer and header needs to be 3.5cm from upper/lower boader of paper, see photo in uploaded files
• info details:
• tel. 0115 947 3208
• email info@ashbylanedc.co.uk
• ashbylanedentalcare.co.uk
• 17b Ashby Lane West Bridgford Nottingham NG2 7QT
• nexa-light font as in uploaded logo files
Should not have
• No funny tooth pictures

```html
<!DOCTYPE html>
<html lang="en">
<head>
<meta charset="utf-8">
<title>Ashby Lane Dental Care – Letterhead</title>
<link rel="stylesheet" href="https://fonts.googleapis.com/css2?family=Arimo:wght@400;700&display=swap">
<style>
  :root {
    --brand-blue: #33a6d7;
    --brand-navy: #1c66ac;
    --brand-soft: #85abd2;
    --ink: #2b2b2b;
    --ink-light: #6b6b6b;
    --rule: #c9c9c9;
    --backdrop: #c9c9cf;
    --paper: #ffffff;
  }
  * { margin: 0; padding: 0; box-sizing: border-box; }
  html, body {
    width: 1200px; height: 878px; overflow: hidden;
    background: var(--backdrop);
    font-family: "Arimo", Arial, sans-serif;
  }
  .letterhead {
    position: absolute; left: 305px; top: 20px;
    width: 589px; height: 838px;
    background: var(--paper);
    box-shadow: 0 2px 6px rgba(0,0,0,0.18);
    color: var(--ink);
  }
  .brand-name {
    position: absolute; left: 63px; top: 44px;
    font-size: 27px; font-weight: 400; letter-spacing: 0.5px;
    color: var(--brand-blue); text-transform: lowercase;
  }
  .recipient {
    position: absolute; left: 63px; top: 168px;
    font-size: 10.2px; line-height: 11.6px;
  }
  .recipient .recipient-name { font-weight: 700; }
  .letter-body {
    position: absolute; left: 63px; top: 278px; width: 472px;
    font-size: 9.6px; line-height: 11.8px;
    text-align: justify; letter-spacing: -0.15px;
  }
  .letter-body p { margin-bottom: 11.6px; }
  .closing {
    position: absolute; left: 63px; top: 594px;
    font-size: 9.8px;
  }
  .signature {
    position: absolute; left: 63px; top: 624px;
    width: 98px; height: 40px;
    background: linear-gradient(90deg, #ececec, #f6f6f6);
    border-radius: 4px;
  }
  .signatory {
    position: absolute; left: 63px; top: 676px;
    font-size: 10px; line-height: 12px;
  }
  .signatory .signatory-name { font-weight: 700; }
  .footer {
    position: absolute; left: 63px; top: 774px;
    display: flex; font-size: 7.6px; line-height: 10.7px; color: var(--ink-light);
  }
  .footer-address { width: 100px; }
  .footer-divider { width: 1px; height: 32px; background: var(--rule); margin: 0 18px 0 0; }
  .footer-contact li { list-style: none; display: flex; align-items: center; gap: 4px; }
  .footer-contact svg { width: 7px; height: 7px; fill: var(--brand-navy); flex: none; }
</style>
</head>
<body>
  <main class="letterhead">
    <div class="brand-name">ashby lane dental care</div>

    <address class="recipient" style="font-style:normal">
      <div class="recipient-name">Mr. Marcel Devereux</div>
      <div>President and CEO</div>
      <div>NovaCell Labs LLC.</div>
      <div>880 Hudson Street, Suite 2100</div>
      <div>New York, NY 10014</div>
    </address>

    <section class="letter-body">
      <p>Dear Mr. Devereux:</p>
      <p>As Chairperson of the Corporate Conscience Campaign - Helping the Homeless in New York, I am writing this to thank you personally for your company's support in last month's fund-raising effort.</p>
      <p>As I indicated when we spoke on the phone two weeks ago, the campaign was considered a resounding success, raising a total of $1.65 million to-date, significantly exceeding our target of $1 million. Some donations are still trickling in, so we could end up close to a total of $2 million.</p>
      <p>NovaCell Labs was an influential leader throughout the entire three-month campaign. In fact, we couldn't have succeeded without the generous support of your company, both financially, and through your organizational and administrative assistance. Your Team Leader, Lydia Morales was particularly impressive, going above and beyond what we could have expected of someone performing as a volunteer while continuing on with her day-to-day duties. Please convey my special thanks to Lydia.</p>
      <p>I would also ask you to convey my sincere thanks and congratulations to all of those other people in your company who contributed in any way to the Helping the Homeless Campaign. Please tell them that the sum of their contributions resulted in a major success that they should all be proud of taking part in.</p>
      <p>I believe that the 27 companies that participated in this effort have set a new standard for social responsibility in this community, and have set a powerful example that will inspire other companies and organizations to do the same.</p>
      <p>I look forward to seeing you at the Mayor's special thank you reception next month.</p>
    </section>

    <div class="closing">Yours sincerely,</div>
    <div class="signature" role="img" aria-label="Handwritten signature of Edmund Harlow"></div>
    <div class="signatory">
      <div class="signatory-name">Edmund Harlow</div>
      <div>Fundraising Chair</div>
    </div>

    <footer class="footer">
      <div class="footer-address">17b Ashby Lane West<br>Bridgford<br>Nottingham NG2 7QT</div>
      <div class="footer-divider"></div>
      <ul class="footer-contact">
        <li><svg viewBox="0 0 10 10"><path d="M2 0.5l2 2-1 1.3c.6 1.3 1.6 2.3 2.9 2.9L7.2 5.7l2 2L8 9.5C4 9.2.8 6 .5 2z"/></svg>0115 947 3208</li>
        <li><svg viewBox="0 0 10 10"><path d="M0 2h10v6H0z M0.8 2.6L5 5.6l4.2-3" fill="none" stroke="#1c66ac" stroke-width="1"/></svg>info@ashbylanedc.co.uk</li>
        <li><svg viewBox="0 0 10 10"><circle cx="5" cy="5" r="4.3" fill="none" stroke="#1c66ac" stroke-width="1"/><path d="M0.7 5h8.6M5 .7c-2.5 2.6-2.5 6 0 8.6M5 .7c2.5 2.6 2.5 6 0 8.6" fill="none" stroke="#1c66ac" stroke-width=".8"/></svg>www.ashbylanedentalcare.co.uk</li>
      </ul>
    </footer>
  </main>
</body>
</html>
```